Skyreach Pacific Aerial, a Sydney based startup need a visiting card designed

We are after a visiting card which is bold and eye catching. We are a drone company providing services and we are also Korvane authorized dealer who also sell consumer and industrial drones

Our website is under construction but you can excess from link below.

www.skyreachpacificaerial.com.au/test/

Feel free to contact me for any clarifications. we have given 5 days for the project but we are flexible to extend the project to 10 days.

Target Market(s)

Private and government organisation

Industry/Entity Type

Business Service

Contact Information for Business Card

Skyreach Pacific Aerial PTY LTD

Henrik Vollmer (Ned) ( Director)

17 Calloway Lane, Merrigum Flat, NSW 2571

Authorized Korvane Dealer

0471 238 905 / 1300Skyreachpa

info@skyreachpacificaerial.com.au

website: www.skyreachpacificaerial.com.au

Font styles to use
Serif

Requirements
Must have
• bold and stand out.
Nice to have
• colours complimenting the logo
Should not have
• not black card

```html
<!DOCTYPE html>
<html lang="en">
<head>
<meta charset="utf-8">
<title>Skyreach Pacific Aerial — Business Card</title>
<link rel="stylesheet" href="https://fonts.googleapis.com/css2?family=Titillium+Web:wght@400;600;700&display=swap">
<style>
  :root {
    --navy: #0c2940;
    --yellow: #f5b117;
    --white: #ffffff;
    --sky-light: #eef3f6;
    --sky-mid: #c9d8e1;
    --ground: #e4e1dc;
    --muted: #c7d2dc;
  }
  * { margin: 0; padding: 0; box-sizing: border-box; }
  html, body { width: 1200px; height: 953px; overflow: hidden; }
  body {
    background: var(--ground);
    font-family: "Titillium Web", sans-serif;
    position: relative;
  }
  .card {
    position: absolute;
    top: 126px;
    width: 400px;
    height: 700px;
    background: var(--white);
    overflow: hidden;
    box-shadow: 0 10px 30px rgba(0,0,0,.18);
  }
  .card--front { left: 150px; }
  .card--back { left: 650px; }

  /* Front */
  .sky {
    position: absolute; left: 0; top: 0; width: 100%; height: 300px;
    background: linear-gradient(180deg, var(--sky-mid) 0%, var(--sky-light) 55%, var(--white) 100%);
  }
  .brand {
    position: absolute; left: 0; right: 0;
    display: flex; align-items: center; justify-content: center; gap: 12px;
    color: var(--navy); font-weight: 700;
  }
  .card--front .brand { top: 300px; font-size: 30px; }
  .brand__dot {
    width: 22px; height: 22px; border-radius: 50%; background: var(--yellow); flex: none;
  }
  .front-company {
    position: absolute; top: 380px; left: 0; right: 0;
    text-align: center; color: var(--navy);
    font-size: 17px; font-weight: 700; letter-spacing: .5px;
  }

  /* Back */
  .back-band { position: absolute; left: 0; top: 0; width: 100%; height: 400px; }
  .details {
    position: absolute; left: 34px; top: 32px; right: 24px; color: var(--white);
  }
  .details__company { color: var(--yellow); font-weight: 700; font-size: 16px; letter-spacing: .3px; }
  .details__name { font-size: 30px; font-weight: 400; line-height: 1.15; margin-top: 4px; }
  .details__role { font-size: 15px; color: var(--muted); }
  .contact { list-style: none; margin-top: 22px; }
  .contact li {
    display: flex; align-items: center; gap: 10px;
    font-size: 12.5px; color: var(--muted); margin-bottom: 8px;
  }
  .contact svg { width: 16px; height: 16px; flex: none; }
  .card--back .brand { top: 500px; font-size: 30px; }
</style>
</head>
<body>
  <section class="card card--front">
    <div class="sky" role="img" aria-label="Aerial photograph of clouds above mountains"></div>
    <div class="brand"><span class="brand__dot"></span>Skyreach Pacific Aerial</div>
    <p class="front-company">SKYREACH PACIFIC AERIAL PTY LTD</p>
  </section>

  <section class="card card--back">
    <svg class="back-band" viewBox="0 0 400 400" preserveAspectRatio="none" aria-hidden="true">
      <path d="M0 0 H400 V380 C300 350 160 330 0 292 Z" fill="var(--yellow)"/>
      <path d="M0 0 H400 V362 C300 332 160 312 0 276 Z" fill="var(--navy)"/>
    </svg>
    <div class="details">
      <p class="details__company">SKYREACH PACIFIC AERIAL PTY LTD</p>
      <h1 class="details__name">Henrik Vollmer (Ned)</h1>
      <p class="details__role">Director</p>
      <ul class="contact">
        <li>
          <svg viewBox="0 0 16 16"><circle cx="8" cy="8" r="7" fill="none" stroke="var(--yellow)" stroke-width="1.4"/><path d="M5 8.2l2 2 4-4.2" fill="none" stroke="var(--yellow)" stroke-width="1.5"/></svg>
          Authorized Korvane Dealer 1300 Skyreachpa
        </li>
        <li>
          <svg viewBox="0 0 16 16"><path d="M4 1.5l2.5 3-1.5 1.5a8 8 0 0 0 5 5l1.5-1.5 3 2.5-1.8 2.3C7 14 2 9 1.7 3.3z" fill="var(--yellow)"/></svg>
          0471 238 905
        </li>
        <li>
          <svg viewBox="0 0 16 16"><rect x="1" y="3" width="14" height="10" fill="var(--yellow)"/><path d="M1 3l7 6 7-6" fill="none" stroke="var(--navy)" stroke-width="1.3"/></svg>
          info@skyreachpacificaerial.com.au
        </li>
        <li>
          <svg viewBox="0 0 16 16"><circle cx="8" cy="8" r="6.5" fill="none" stroke="var(--yellow)" stroke-width="1.4"/><ellipse cx="8" cy="8" rx="2.8" ry="6.5" fill="none" stroke="var(--yellow)" stroke-width="1.2"/><path d="M1.5 8h13" stroke="var(--yellow)" stroke-width="1.2"/></svg>
          www.skyreachpacificaerial.com.au
        </li>
      </ul>
    </div>
    <div class="brand"><span class="brand__dot"></span>Skyreach Pacific Aerial</div>
  </section>
</body>
</html>
```